Packaging design pot 500gr Polynesian honey

Task Description

Concept of design:

"This Polynesian island is a small piece of paradise nestled in the South Pacific, away from any form of civilization ( ideal place for producing honey of excellence )
= Images / symbols that induces dreaming)); (100% organic, 100% natural organic Honey logo)
Elegant, subtle , eyes catching, NO pictures of bees , Simple colors: BLACK, GOLD, WHITE, tranparency . (Designer discretion)
(Bio label optional )

the Labels: Hex1 product of TAHITI header: VELINOA HONEY (brand name) MAY USE all images herein below , free of copyright (Macro coconut flower, coconut white sand beach, exoticism; 500 gr; text on back (see attached text); Position the bar code vertically on the back; Mandatory address: Website on the back, infocontact, registration number.

500g pot :
HEIGHT With cap 12.00cm Without cap 11.85 cm
outside diameter 7.24cm
Label height should only be = 5, 1 cm x height
See the container with black cap.

Deadline
March 15, 2018 ( postpone if needed )
Updates

To all participants, i have added a personal photo you may want to consider in your creative process. If the upper section of the photo is exploited, I thought it has something interesting to bring: blue sky on the background including a shadow ot the coconut leaves, ( no bees please).

Finally i have added the colour of Velinoa Honey

Dear participants, I have updated two files to be taken into account onward : 1) final text: in French ; the replicate is English for the English version valid with the identical Graphic design 2) the true colours of Velinoa Honey, for your consideration. I thought that with the help of day light i could enhance its true body colour. Best regards, Mr KOR

Target Market(s)

Target the Asian market , Onward The US MARKET, (LUXURY oriented)

Font styles to use
Serif

Colors

Designer to choose colors to be used in the design.

Requirements
Must have
• Website address on the back, infocontact, registration number,
• texte ( summary )
• coconut tree honey ( ORIGIN )
• Color code : BLACK , GOLD , light , transparency
• COLORS THAT MATCH COLOR OF THE HONEY : DARK RED AMBER SEE IMAGE ATTACHED
Nice to have
• A matching logo
• A 400g Squezze bottle format ;
• h18.5*d7.8*c3.2(cm)
Should not have
• No Bees

```html
<!DOCTYPE html>
<html lang="en">
<head>
<meta charset="utf-8">
<title>Cocotier Tahiti – Velinoa Honey 500 gr label</title>
<link rel="stylesheet" href="https://fonts.googleapis.com/css2?family=Arvo:wght@700&family=Mulish:wght@300;400&family=Amaranth:wght@400&family=Open+Sans:wght@700&display=swap">
<style>
  :root {
    --page-bg: #e4e4e4;
    --label-dark: #3b3837;
    --tag-dark: #34302f;
    --white: #ffffff;
    --gold: #f2c316;
    --amber: #f39a1e;
    --photo-rose: #b5566e;
    --photo-coral: #e8886a;
    --photo-peach: #f2b27a;
    --photo-sun: #f6c340;
  }
  * { margin: 0; padding: 0; box-sizing: border-box; }
  html, body {
    width: 810px;
    height: 1200px;
    overflow: hidden;
    background: var(--page-bg);
  }
  .canvas {
    position: relative;
    width: 810px;
    height: 1200px;
  }

  /* Hang tag */
  .hang-tag {
    position: absolute;
    left: 315px;
    top: 60px;
    width: 180px;
    height: 270px;
    background: var(--tag-dark);
    border-radius: 18px;
    display: flex;
    flex-direction: column;
    align-items: center;
  }
  .hang-tag__hole {
    margin-top: 22px;
    width: 16px;
    height: 16px;
    border-radius: 50%;
    background: var(--page-bg);
  }
  .hang-tag__mark {
    margin-top: 70px;
    width: 30px;
    height: 30px;
    border-radius: 50%;
    background: var(--gold);
  }
  .hang-tag__brand {
    margin-top: 18px;
    font-family: "Mulish", sans-serif;
    font-weight: 400;
    font-size: 22px;
    line-height: 1.15;
    letter-spacing: 2px;
    text-align: center;
    color: var(--gold);
  }

  /* Jar label */
  .jar-label {
    position: absolute;
    left: 55px;
    top: 420px;
    width: 700px;
    height: 645px;
    overflow: hidden;
  }
  .jar-label__header {
    height: 325px;
    background: var(--label-dark);
    text-align: center;
    padding-top: 62px;
  }
  .product-name {
    font-family: "Arvo", serif;
    font-weight: 700;
    font-size: 56px;
    letter-spacing: 12px;
    color: var(--white);
    line-height: 1;
    padding-left: 12px;
  }
  .product-origin {
    margin-top: 16px;
    font-family: "Mulish", sans-serif;
    font-weight: 300;
    font-size: 64px;
    color: var(--gold);
    line-height: 1;
  }
  .product-tagline {
    margin-top: 22px;
    font-family: "Amaranth", sans-serif;
    font-size: 34px;
    color: var(--amber);
    line-height: 1;
  }
  .jar-label__photo {
    position: relative;
    height: 320px;
    background: linear-gradient(100deg, var(--photo-sun) 0%, var(--photo-rose) 30%, var(--photo-coral) 55%, var(--photo-peach) 75%, var(--photo-sun) 100%);
  }
  .net-weight {
    position: absolute;
    left: 306px;
    top: 254px;
    font-family: "Open Sans", sans-serif;
    font-weight: 700;
    font-size: 19px;
    color: var(--white);
  }
</style>
</head>
<body>
  <main class="canvas">
    <div class="hang-tag">
      <span class="hang-tag__hole"></span>
      <span class="hang-tag__mark"></span>
      <p class="hang-tag__brand">VELINOA<br>HONEY</p>
    </div>

    <section class="jar-label">
      <header class="jar-label__header">
        <h1 class="product-name">COCOTIER</h1>
        <p class="product-origin">TAHITI</p>
        <p class="product-tagline">Honey From Flowers Tahiti</p>
      </header>
      <div class="jar-label__photo" role="img" aria-label="Coconuts and palm fronds in warm rose and golden sunset tones">
        <span class="net-weight">500 gr</span>
      </div>
    </section>
  </main>
</body>
</html>
```